Innovative Health and Beauty business needs a clean Brand Image -

We need a logo designed and packaging for a new company. We are developing safe, easy to use, and reliable products to help people in health and beauty industry. We would like creative, clean, and elegant branding to elevate brand integrity and customer service focus.

```html
<!DOCTYPE html>
<html lang="en">
<head>
<meta charset="utf-8">
<title>Lucenta – Packaging Dieline</title>
<link rel="stylesheet" href="https://fonts.googleapis.com/css2?family=Jost:wght@300;400;500&family=Source+Sans+3:wght@400&display=swap">
<style>
  :root {
    --paper: #ffffff;
    --ink: #000000;
    --line: #3a3a3a;
    --panel-tint: #f5f8fd;
    --text-dark: #1f1f1f;
    --text-grey: #5a5a5a;
    --blue-deep: #0a5fb8;
    --blue-mid: #1a84dc;
    --blue-bright: #0a8ae6;
    --purple-soft: #9a92d8;
    --pink-soft: #d89ac8;
    --cyan: #06b6ec;
    --cyan-light: #7fd4f6;
    --navy: #1a2e7a;
  }
  html, body {
    margin: 0;
    padding: 0;
    width: 705px;
    height: 1200px;
    overflow: hidden;
    background: var(--paper);
  }
  .canvas {
    position: relative;
    width: 705px;
    height: 1200px;
    background: var(--paper);
    font-family: "Source Sans 3", sans-serif;
  }

  /* Brand tile */
  .brand-tile {
    position: absolute;
    left: 219px; top: 64px;
    width: 260px; height: 256px;
    background: var(--ink);
    display: flex;
    align-items: center;
    justify-content: center;
  }
  .brand-tile .wordmark {
    font-family: "Jost", sans-serif;
    font-weight: 300;
    font-size: 62px;
    color: var(--panel-tint);
    letter-spacing: 1px;
  }

  /* Dieline pieces */
  .flap {
    position: absolute;
    border: 1px solid var(--line);
    box-sizing: border-box;
    background: var(--paper);
  }
  .flap--dust-left-top   { left: 65px;  top: 401px; width: 108px; height: 123px; }
  .flap--dust-right-top  { left: 516px; top: 401px; width: 108px; height: 123px; }
  .flap--side-left       { left: 65px;  top: 675px; width: 108px; height: 143px; }
  .flap--side-right      { left: 516px; top: 675px; width: 106px; height: 143px; }
  .flap--tuck-left       { left: 65px;  top: 817px; width: 100px; height: 113px; border-radius: 0 0 26px 26px; }
  .flap--tuck-right      { left: 523px; top: 817px; width: 100px; height: 113px; border-radius: 0 0 26px 26px; }
  .flap--bottom-tuck     { left: 173px; top: 960px; width: 343px; height: 143px; border-radius: 0 0 44px 44px; }

  .panel {
    position: absolute;
    left: 172px;
    width: 344px;
    border: 1px solid var(--line);
    box-sizing: border-box;
    overflow: hidden;
  }
  .panel--front  { top: 390px; height: 143px; }
  .panel--top    { top: 532px; height: 144px;
                   background: radial-gradient(ellipse at 50% 55%, #ffffff 20%, var(--panel-tint) 75%); }
  .panel--bottom { top: 675px; height: 143px; }
  .panel--back   { top: 817px; height: 144px; background: var(--panel-tint); }

  .panel-art {
    position: absolute;
    inset: 0;
  }
  .panel--front .panel-art {
    background:
      linear-gradient(152deg, transparent 58%, var(--blue-bright) 58.2%),
      linear-gradient(100deg, var(--pink-soft) 0%, var(--blue-deep) 22%, var(--purple-soft) 45%, var(--blue-mid) 70%, var(--blue-deep) 100%);
  }
  .panel--bottom .panel-art {
    background:
      linear-gradient(-28deg, transparent 58%, var(--cyan) 58.2%),
      linear-gradient(80deg, var(--cyan) 0%, var(--cyan-light) 35%, var(--cyan) 60%, var(--navy) 85%, var(--cyan-light) 100%);
  }

  .product-title {
    position: absolute;
    font-family: "Jost", sans-serif;
    font-weight: 500;
    font-size: 12.5px;
    color: #ffffff;
    letter-spacing: 0.2px;
    white-space: nowrap;
  }
  .panel--front .product-title { right: 8px; top: 6px; }
  .panel--bottom .product-title { right: 8px; top: 16px; transform: rotate(180deg); }

  .panel-wordmark {
    position: absolute;
    font-family: "Jost", sans-serif;
    font-weight: 300;
    font-size: 15px;
    color: #ffffff;
  }
  .panel--front .panel-wordmark { right: 18px; top: 106px; }
  .panel--bottom .panel-wordmark { left: 14px; top: 14px; transform: rotate(180deg); }

  .back-copy {
    position: absolute;
    left: 23px; top: 26px;
    width: 160px;
    font-size: 8.1px;
    line-height: 10.4px;
    color: var(--text-dark);
  }
  .back-copy p { margin: 0 0 10px; }
  .back-contact {
    position: absolute;
    left: 201px; top: 27px;
    font-size: 8.1px;
    line-height: 10.4px;
    color: var(--text-grey);
  }
  .back-wordmark {
    position: absolute;
    right: 14px; top: 113px;
    font-family: "Jost", sans-serif;
    font-weight: 300;
    font-size: 14px;
    color: var(--ink);
  }
</style>
</head>
<body>
<div class="canvas">

  <div class="brand-tile">
    <span class="wordmark">lucenta</span>
  </div>

  <div class="flap flap--dust-left-top"></div>
  <div class="flap flap--dust-right-top"></div>
  <div class="flap flap--side-left"></div>
  <div class="flap flap--side-right"></div>
  <div class="flap flap--tuck-left"></div>
  <div class="flap flap--tuck-right"></div>
  <div class="flap flap--bottom-tuck"></div>

  <section class="panel panel--front">
    <div class="panel-art" role="img" aria-label="Geometric triangle mosaic in pink, purple and blue tones"></div>
    <h1 class="product-title">INFLATABLE SHAMPOO BOWL</h1>
    <span class="panel-wordmark">lucenta</span>
  </section>

  <section class="panel panel--top"></section>

  <section class="panel panel--bottom">
    <div class="panel-art" role="img" aria-label="Geometric triangle mosaic in cyan, light blue and navy tones"></div>
    <h2 class="product-title">INFLATABLE SHAMPOO BOWL</h2>
    <span class="panel-wordmark">lucenta</span>
  </section>

  <section class="panel panel--back">
    <div class="back-copy">
      <p>Lorem ipsum dolor sit amet, consectetuer adipiscing elit, sed diam nonummy nibh euismod tincidunt ut laoreet dolore magna</p>
      <p>aliquam erat volutpat. Ut wisi enim ad minim veniam, quis nostrud exerci tation ullamcorper suscipit lobortis nisl ut aliquip</p>
    </div>
    <div class="back-contact">Lorem ipsum dolor sit<br>Address 123 4567</div>
    <span class="back-wordmark">lucenta</span>
  </section>

</div>
</body>
</html>
```